Gladly Call Corwin Consulting needs a new and exciting customer online experience (Webpage)

Gladly Call Corwin is a new and exciting IT and Telecoms business. We aim to help business with all of its technology needs.

The business has only been around less than 12 months and a page was developed to give some online presence, but now its time for a refresh. The page is very bland and boring. It needs some creative zing to give it that pop whilst maintaining a professional appeal.

Our current page can be found at www.gladlycallcorwin.example.au

I have included below some of our current marketing. I've included our business cards and some of messages on hold we are running.

Target Market(s)

Small to medium business, small enterprise

Industry/Entity Type

Business

Number of Pages Required

5+ page

Font styles to use
Sans Serif

Requirements
Must have
• The page must have some colour. IT and Telecoms can be mundane and boring. We want people to be engaged in their IT and Telecoms. We want them to feel as passionate about their IT and Telecoms as we do.
• It must have the following pages: Home, About Us, Services We provide, Contact Us and our Blog Page.
• The contact us should have an option to complete an online form which is delivered to our enquiries email.
• We would also like to have our social media links for Chatterbook, WorkWeave and Quorra plus. The pages must also contain a link to our privacy policy located near the bottom of the page

```html
<!DOCTYPE html>
<html lang="en">
<head>
<meta charset="utf-8">
<title>Gladly Call Corwin Consulting</title>
<link href="https://fonts.googleapis.com/css2?family=Raleway:wght@300;400;500;600;700&display=swap" rel="stylesheet">
<style>
:root{
  --red:#db1535;
  --blue:#27aae1;
  --ink:#1c1c1c;
  --muted:#9a9a9a;
  --band:#f2f2f2;
  --footer:#15202b;
  --footer-deep:#0e161e;
  --footer-text:#7f8a94;
  --white:#ffffff;
}
*{margin:0;padding:0;box-sizing:border-box}
html,body{width:992px;height:1200px;overflow:hidden;background:var(--white)}
body{font-family:"Raleway",sans-serif;color:var(--ink);position:relative}
.abs{position:absolute}

/* header */
.site-header{left:0;top:0;width:992px;height:63px;background:var(--white)}
.brand{left:63px;top:20px;font-weight:600;font-size:13px;line-height:14px;color:#2a2a4a;text-align:center}
.main-nav{right:50px;top:0;display:flex;height:63px}
.main-nav a{display:block;height:63px;line-height:58px;padding:0 15px;font-size:13px;color:#222;text-decoration:none;position:relative}
.main-nav a.active{background:var(--blue);color:var(--white);padding:0 16px}
.main-nav a.active::after{content:"";position:absolute;left:50%;bottom:0;margin-left:-5px;border:5px solid transparent;border-bottom-color:var(--white)}

/* hero */
.hero{left:0;top:63px;width:992px;height:305px;background:var(--red)}
.hero-title{left:62px;top:153px;font-weight:300;font-size:58px;line-height:64px;color:var(--white);letter-spacing:1px}
.hero-sub{left:62px;top:282px;font-weight:400;font-size:25px;color:var(--white)}
.hero-tagline{left:62px;top:329px;font-size:13.5px;color:var(--white)}
.hero-visual{left:506px;top:173px;width:422px;height:247px;border-radius:10px 10px 4px 4px;background:linear-gradient(180deg,#1e2a33 0%,#9cc43e 18%,#9cc43e 86%,#cfd3d6 100%)}
.slider-dots{left:457px;top:448px;display:flex;gap:3px}
.slider-dots span{width:23px;height:3px;background:#e3e3e3}
.slider-dots span.on{background:#111}

/* call band */
.call-band{left:0;top:470px;width:992px;height:106px;background:var(--band)}
.call-title{left:137px;top:498px;font-weight:400;font-size:28px;letter-spacing:.5px;color:#222}
.call-sub{left:137px;top:530px;font-size:16px;color:var(--blue)}
.ask-btn{left:793px;top:509px;width:61px;height:34px;background:var(--white);border-radius:2px;font-size:11px;font-weight:600;line-height:34px;text-align:center;color:#222}

/* features */
.feature{width:275px;top:662px}
.feature-art{width:132px;height:132px;border-radius:50%;margin:0 auto}
.feature h3{margin-top:38px;font-size:13px;font-weight:600;text-align:center;letter-spacing:.3px;color:#111}
.feature p{margin-top:16px;font-size:11px;line-height:21px;color:var(--muted)}
.feature p a{color:var(--blue);text-decoration:none;border-bottom:1px solid var(--blue);font-weight:500}
.art-tools{background:radial-gradient(circle,#2f7f9a 0%,#2a9fbf 55%,#f3c335 100%)}
.art-savings{background:radial-gradient(circle,#f7b733 0%,#2a8ea8 75%)}
.art-partner{background:radial-gradient(circle,#f4b12d 0%,#1d3a4f 65%)}

/* footer */
.site-footer{left:0;top:962px;width:992px;height:192px;background:var(--footer)}
.footer-tab{left:469px;top:962px;width:53px;height:3px;background:var(--blue)}
.footer-brand{left:66px;top:1032px;width:116px;text-align:center;font-size:12px;line-height:13px;font-weight:500;color:var(--white)}
.footer-col{top:996px}
.footer-col h4{font-size:13px;font-weight:700;color:var(--white);letter-spacing:.3px;margin-bottom:12px}
.posts li{list-style:none;font-size:10.5px;color:var(--footer-text);line-height:21px;padding-left:12px;position:relative}
.posts li::before{content:"";position:absolute;left:2px;top:9px;width:3px;height:3px;border-radius:50%;background:var(--footer-text)}
.contact-line{display:flex;align-items:center;font-size:10.5px;color:var(--footer-text);height:23px}
.contact-line svg{width:14px;height:14px;margin-right:12px;flex:none}
.legal{left:0;top:1154px;width:992px;height:46px;background:var(--footer-deep)}
.legal-text{left:62px;top:1174px;font-size:10.5px;color:#5d6873}
</style>
</head>
<body>

<header class="site-header abs">
  <div class="brand abs">Gladly Call Corwin<br>Consulting</div>
  <nav class="main-nav abs">
    <a class="active" href="#">Home</a>
    <a href="#">About Us</a>
    <a href="#">Our Services</a>
    <a href="#">Contact Us</a>
    <a href="#">Blog</a>
  </nav>
</header>

<section class="hero abs"></section>
<h1 class="hero-title abs">GLADLY CALL<br>CORWIN</h1>
<div class="hero-sub abs">consulting</div>
<p class="hero-tagline abs">Making IT and Telecommunications simple for business.</p>
<div class="hero-visual abs" role="img" aria-label="Laptop showing a flat business illustration with charts, calendar and briefcase"></div>
<div class="slider-dots abs"><span class="on"></span><span></span><span></span></div>

<section class="call-band abs"></section>
<h2 class="call-title abs">MAKING IT AND TELECOMMUNICATIONS</h2>
<div class="call-sub abs">SIMPLE FOR BUSINESS</div>
<div class="ask-btn abs">Ask!</div>

<article class="feature abs" style="left:62px">
  <div class="feature-art art-tools" role="img" aria-label="Illustration of tools surrounded by tech service icons"></div>
  <h3>WHAT CAN WE HELP WITH</h3>
  <p>Cras accumsan pellentesque dignissim. Duis volutpat odio cursus. Vivamus rhoncus, arcu ac faucibus laoreet, lorem tellus varius lectus... <a href="#">read more</a></p>
</article>
<article class="feature abs" style="left:358px">
  <div class="feature-art art-savings" role="img" aria-label="Illustration of a piggy bank with clocks and money"></div>
  <h3>HOW CAN WE HELP</h3>
  <p>Cras accumsan pellentesque dignissim. Duis volutpat odio cursus. Vivamus rhoncus, arcu ac faucibus laoreet, lorem tellus varius lectus... <a href="#">read more</a></p>
</article>
<article class="feature abs" style="left:654px">
  <div class="feature-art art-partner" role="img" aria-label="Illustration of a handshake surrounded by business icons"></div>
  <h3>WHY NOT CONTACT US</h3>
  <p>Cras accumsan pellentesque dignissim. Duis volutpat odio cursus. Vivamus rhoncus, arcu ac faucibus laoreet, lorem tellus varius lectus... <a href="#">read more</a></p>
</article>

<footer class="site-footer abs"></footer>
<div class="footer-tab abs"></div>
<div class="footer-brand abs">Gladly Call Corwin<br>Consulting</div>

<div class="footer-col abs" style="left:284px">
  <h4>RECENT POSTS</h4>
  <ul class="posts">
    <li>Nullam nisl nibh, porta et nunc vel</li>
    <li>Nullam nisl nibh, porta et nunc vel</li>
    <li>Nullam nisl nibh, porta et nunc vel</li>
    <li>Nullam nisl nibh, porta et nunc vel</li>
  </ul>
</div>

<div class="footer-col abs" style="left:506px">
  <h4>CONTACT</h4>
  <div class="contact-line">
    <svg viewBox="0 0 14 14"><path d="M7 0.5a4.5 4.5 0 0 0-4.5 4.5c0 3.3 4.5 8.5 4.5 8.5s4.5-5.2 4.5-8.5A4.5 4.5 0 0 0 7 0.5z" fill="#27aae1"/><circle cx="7" cy="5" r="1.7" fill="#15202b"/></svg>
    412 Harbour Road Seacliff North SA
  </div>
  <div class="contact-line">
    <svg viewBox="0 0 14 14"><path d="M1 5c0-2 2.5-3 6-3s6 1 6 3v1.2h-3V4.8H4v1.4H1z" fill="#27aae1"/><path d="M3 7h8l1.5 5h-11z" fill="#27aae1"/><circle cx="7" cy="9.5" r="1.3" fill="#15202b"/></svg>
    (08) 7000 3182
  </div>
  <div class="contact-line">
    <svg viewBox="0 0 14 14"><rect x="0.5" y="2.5" width="13" height="9" fill="#27aae1"/><path d="M0.5 2.5 7 7.5l6.5-5" fill="none" stroke="#15202b" stroke-width="1"/></svg>
    enquiries@gladlycallcorwin.example.au
  </div>
</div>

<div class="footer-col abs" style="left:728px">
  <h4>MAP</h4>
  <div class="contact-line">
    <svg viewBox="0 0 14 14"><path d="M1 2.5 5 1v10.5L1 13z M5.5 1l3 1.5V13l-3-1.5z M9 2.5 13 1v10.5L9 13z" fill="#27aae1"/></svg>
    412 Harbour Road Seacliff North SA
  </div>
</div>

<div class="legal abs"></div>
<p class="legal-text abs">2014 Gladly Call Corwin. All rights reserved.</p>

</body>
</html>
```